business card for a massage therapy practice named 'Meadow and Willow Massage Studio'

I really need a trendy, yet easy on the eyes business card to complement my logo. Ideally with some gold or rose gold foil work.

My uploaded file of the logo I have in horizontal but I have a vertical version as well. Another color that is used in the website is a blush pink here and there. I'd like to see some trendy tropical leaves in the design.

```html
<!DOCTYPE html>
<html lang="en">
<head>
<meta charset="utf-8">
<title>Meadow and Willow Massage Studio — Business Card</title>
<link href="https://fonts.googleapis.com/css2?family=Roboto:wght@400;500&display=swap" rel="stylesheet">
<style>
  :root {
    --bg: #2b2b2b;
    --tan: #9c8763;
    --mint: #86cfb8;
    --mint-dark: #5fa893;
    --paper: #ffffff;
    --ink: #1e1e1e;
  }
  * { box-sizing: border-box; margin: 0; padding: 0; }
  html, body { width: 1200px; height: 900px; overflow: hidden; }
  body {
    background: var(--bg);
    font-family: "Roboto", Arial, sans-serif;
    position: relative;
  }
  .card {
    position: absolute;
    width: 600px;
    height: 343px;
    box-shadow: 0 12px 30px rgba(0,0,0,.45);
    overflow: hidden;
  }
  .card-front {
    left: 70px; top: 80px;
    background: var(--tan);
  }
  .card-back {
    left: 530px; top: 477px;
    background: var(--tan);
  }
  .wordmark {
    display: flex;
    align-items: center;
    gap: 14px;
    color: var(--ink);
    font-weight: 500;
  }
  .wordmark-dot {
    width: 34px; height: 34px;
    border-radius: 50%;
    flex: none;
  }
  .card-front .wordmark {
    position: absolute;
    left: 0; right: 0; top: 128px;
    justify-content: center;
    font-size: 30px;
  }
  .card-front .wordmark-dot { background: var(--paper); }
  .front-web {
    position: absolute;
    left: 0; right: 0; bottom: 44px;
    text-align: center;
    color: var(--paper);
    font-size: 14px;
    letter-spacing: .3px;
  }
  .back-shape { position: absolute; inset: 0; }
  .card-back .wordmark {
    position: absolute;
    left: 40px; top: 100px;
    width: 240px;
    font-size: 20px;
    line-height: 1.25;
  }
  .card-back .wordmark-dot { background: var(--tan); width: 26px; height: 26px; }
  .contact-list {
    position: absolute;
    left: 40px; top: 214px;
    list-style: none;
    display: flex; flex-direction: column; gap: 7px;
  }
  .contact-item {
    display: flex; align-items: center; gap: 12px;
    font-size: 14px; color: var(--ink);
  }
  .contact-icon {
    width: 22px; height: 22px;
    background: var(--tan);
    display: flex; align-items: center; justify-content: center;
  }
  .name-ribbon {
    position: absolute;
    left: 312px; top: 34px;
    width: 288px; height: 62px;
    background: var(--mint);
    color: var(--paper);
    padding: 12px 0 0 52px;
  }
  .ribbon-fold {
    position: absolute;
    left: 312px; top: 96px;
  }
  .person-name { font-size: 18px; font-weight: 500; letter-spacing: .5px; }
  .person-role { font-size: 11px; margin-top: 2px; }
  .address {
    position: absolute;
    right: 40px; top: 226px;
    width: 210px;
    text-align: center;
    color: var(--paper);
    font-size: 13px;
    line-height: 1.45;
  }
  .address svg { display: block; margin: 0 auto 6px; }
</style>
</head>
<body>

  <section class="card card-front" aria-label="Card front">
    <div class="wordmark">
      <span class="wordmark-dot"></span>
      <span>Meadow and Willow Massage Studio</span>
    </div>
    <p class="front-web">www.meadowwillow.com</p>
  </section>

  <section class="card card-back" aria-label="Card back">
    <svg class="back-shape" width="600" height="343" viewBox="0 0 600 343">
      <defs>
        <filter id="edge-shadow" x="-10%" y="-10%" width="120%" height="120%">
          <feDropShadow dx="3" dy="0" stdDeviation="4" flood-opacity=".3"/>
        </filter>
      </defs>
      <polygon points="0,0 300,0 340,343 0,343" fill="var(--paper)" filter="url(#edge-shadow)"/>
    </svg>

    <div class="name-ribbon">
      <p class="person-name">ELLIS MARLOW</p>
      <p class="person-role">Founder &amp; Director</p>
    </div>
    <svg class="ribbon-fold" width="34" height="16" viewBox="0 0 34 16">
      <polygon points="0,0 34,0 34,16" fill="var(--mint-dark)"/>
    </svg>

    <div class="wordmark">
      <span class="wordmark-dot"></span>
      <span>Meadow and Willow<br>Massage Studio</span>
    </div>

    <ul class="contact-list">
      <li class="contact-item">
        <span class="contact-icon">
          <svg width="12" height="12" viewBox="0 0 24 24"><path fill="#fff" d="M6.6 10.8a15 15 0 0 0 6.6 6.6l2.2-2.2a1 1 0 0 1 1-.25 11.4 11.4 0 0 0 3.6.6 1 1 0 0 1 1 1V20a1 1 0 0 1-1 1A17 17 0 0 1 3 4a1 1 0 0 1 1-1h3.5a1 1 0 0 1 1 1c0 1.250.2 2.450.6 3.6a1 1 0 0 1-.25 1z"/></svg>
        </span>555-014-2288
      </li>
      <li class="contact-item">
        <span class="contact-icon">
          <svg width="12" height="12" viewBox="0 0 24 24"><rect x="3" y="8" width="18" height="12" rx="2" fill="none" stroke="#fff" stroke-width="2"/><path d="M6 8V5h12v3" fill="none" stroke="#fff" stroke-width="2"/><circle cx="12" cy="14" r="2.5" fill="#fff"/></svg>
        </span>555-014-2288
      </li>
      <li class="contact-item">
        <span class="contact-icon">
          <svg width="12" height="12" viewBox="0 0 24 24"><rect x="2" y="5" width="20" height="14" fill="none" stroke="#fff" stroke-width="2"/><path d="M2 5l10 8 10-8" fill="none" stroke="#fff" stroke-width="2"/></svg>
        </span>hello@meadowwillow.com
      </li>
      <li class="contact-item">
        <span class="contact-icon">
          <svg width="12" height="12" viewBox="0 0 24 24"><circle cx="12" cy="12" r="9" fill="none" stroke="#fff" stroke-width="2"/><path d="M3 12h18M12 3c3 3 3 15 0 18M12 3c-3 3-3 15 0 18" fill="none" stroke="#fff" stroke-width="1.6"/></svg>
        </span>www.meadowwillow.com
      </li>
    </ul>

    <div class="address">
      <svg width="12" height="16" viewBox="0 0 24 32"><path fill="#fff" d="M12 0a11 11 0 0 0-11 11c0 8 11 21 11 21s11-13 11-21A11 11 0 0 0 12 0zm0 15a4 4 0 1 1 0-8 4 4 0 0 1 0 8z"/></svg>
      4821 Harbor Lane,<br>Palm Cove, Florida, 34951
    </div>
  </section>

</body>
</html>
```